company, product, services, opportunity presentation

Lumivanta is a Payment Services Processor with value added product and services. We are focusing on the Payment Industry, Retail Merchants and Financial institutions. We have built total solution on QMO cloud to provide API based payment solutions such as Issuing of cards, Acquiring of payment transactions, Fraud prevention, Ecommerce, with customer facing APPs to provide dynamic virtual payment , 2FA and Passwordless sign in. Our focus is B2B .
We are developing our sales/investor pitch deck with slides covering company information, Market challengers (problems) that we are solving , Opportunities in the regional markets as well as global addressable Market for Payment cards. Lumivanta Product and services offerings to meet these challenges and opportunities.
Total Addressable Market statistics and data. Specific to virtual payment cards, Second factor authentication and digital ID (passwordless). Primarily data and justification for reducing Ecommerce card abandonment and increasing Authorization rates
Lumivanta Team and advisors’ slide. Current pipeline and customers. Use cases or case studies. Highlighting competitive advantage and USP. target clients and current pipline. Financials and projected spend in the next 2 years including target amount to raise fund. Solution and services slides and timeine of activities /roadmap
We need a PPT design to project better look and feel, crisp and eye catching graphic and design of the slides. clearer representation of key or salient points in all slides and information.

Target Market(s)

Financial Institutions, Retail (Merchants), Fintechs, Transportation

Industry/Entity Type

Cards and Payments Industry . Fraud prevention . Digital ID

Font styles to use
Sans Serif

Colors
F0912C
F2A743
F7CA91
FBE8D2
FDF5EE
EE7325
F08F49
F5BC92
FAE3D3
FDF4ED
A7469A
B969AE
D3A5CF
EDDBEB
F8F0F9
6B429C
8869AF
B7A5CE
E3DAEB
F3F0F8

Requirements
Must have
• problem to be solved, market challenges, market opportunities, product features and functionality. Use cases, Financial spend and funding. Team members and advisors. Timeline of roadmap for 2 years. competitive advantage and USP. Benefits to each customer segments
Nice to have
• Provision for future development on product and services. potentially covering other target markets such as Airlines, Insurance

```html
<!DOCTYPE html>
<html lang="en">
<head>
<meta charset="utf-8">
<title>Lumivanta — Business Solutions &amp; Client Verticals</title>
<link rel="stylesheet" href="https://fonts.googleapis.com/css2?family=Figtree:wght@400;500;600;700;800&display=swap">
<style>
  :root{
    --plum:#7E2A7D;
    --orange:#F0912C;
    --ink:#4A4A55;
    --muted:#8E8E98;
    --charcoal:#3E3F4B;
    --mist:#F1F1F5;
    --line:#E6E6EC;
    --white:#FFFFFF;
  }
  *{box-sizing:border-box;margin:0;padding:0}
  html,body{width:1010px;height:1200px;overflow:hidden}
  body{background:var(--plum);font-family:"Figtree",Arial,sans-serif;color:var(--ink);position:relative}
  ul{list-style:none}

  .slide{position:absolute;left:62px;width:886px;height:498px;background:var(--white);box-shadow:0 20px 30px rgba(45,5,45,.35)}
  .slide--first{top:62px}
  .slide--second{top:636px;background:var(--mist)}

  /* sidebar */
  .verticals{position:absolute;left:0;top:0;width:153px;height:100%;background:var(--mist)}
  .slide--second .verticals{background:var(--white)}
  .verticals__head{height:78px;background:var(--plum);color:var(--white);font-weight:800;font-size:13px;line-height:16.5px;padding:31px 0 0 35px;letter-spacing:.1px}
  .verticals__notch{position:absolute;left:132px;top:77px;width:21px;height:22px;background:var(--plum);clip-path:polygon(0 0,100% 0,100% 100%)}
  .vertical{position:absolute;left:34px;display:flex;align-items:center;gap:7px;font-size:10.5px;font-weight:500;color:var(--muted);line-height:13px;transform:translateY(-50%)}
  .vertical--indent span{margin-left:5px}
  .vertical__icon{width:25px;height:25px;border-radius:4px;background:var(--plum);display:flex;align-items:center;justify-content:center;flex:none}
  .vertical__icon svg{width:17px;height:17px}

  /* title */
  .headline{position:absolute;left:153px;right:0;top:28px;text-align:center;font-size:26.5px;font-weight:800;color:var(--plum);letter-spacing:-.2px}
  .headline em{font-style:normal;color:var(--orange)}

  /* service columns */
  .service{position:absolute;top:77px;height:213px;background:var(--white);border:1px solid var(--line);border-radius:3px;box-shadow:0 2px 4px rgba(0,0,0,.05)}
  .service__head{position:absolute;left:-1px;right:-1px;top:-1px;height:76px;background:var(--plum);display:flex;align-items:flex-start;justify-content:center;gap:10px;padding-top:13px;clip-path:polygon(0 0,100% 0,100% 100%,calc(100% - 20px) 80%,20px 80%,0 100%);border-radius:3px 3px 0 0}
  .service--accent .service__head{background:var(--orange)}
  .service__head svg{width:34px;height:34px;flex:none}
  .service__head h3{color:var(--white);font-size:10.3px;font-weight:800;line-height:12.5px;text-transform:uppercase;padding-top:4px}
  .service__rows{position:absolute;left:0;right:0;top:60px}
  .service__row{height:37px;display:flex;align-items:center;gap:9px;padding-left:10px;font-size:8.5px;color:var(--ink);border-top:1px solid var(--line);line-height:10px}
  .service__row:first-child{height:40px;border-top:0}
  .service__row svg{width:10px;height:8px;flex:none}
  .service--acquirer .service__row{gap:6px;padding-left:9px;font-size:8.2px}
  .service__row .pair{display:flex;gap:4px}
  .service__row .pair span:first-child{width:59px}
  .service__row .pair span:last-child{width:57px}
  .service--networks .service__row{justify-content:center;padding-left:0;font-size:12px;font-weight:800;color:var(--plum)}

  .slide--second .service{top:80px;height:218px;border:0;border-radius:3px;box-shadow:0 2px 5px rgba(0,0,0,.06)}
  .slide--second .service__head{height:64px;clip-path:none;align-items:center;padding-top:0;top:0;left:0;right:0}
  .slide--second .service__rows{top:64px}
  .slide--second .service__row,.slide--second .service__row:first-child{height:38.5px;border-top:1px solid var(--line)}
  .slide--second .service__row:first-child{border-top:0}

  /* capabilities strip */
  .capabilities{position:absolute;left:187px;top:312px;width:680px;height:52px;background:var(--mist);border-radius:26px}
  .capability{display:flex;align-items:center;gap:6px;font-size:8.5px;line-height:10px;color:var(--ink);position:absolute;transform:translateY(-50%);top:50%}
  .capability__dot{width:20px;height:20px;border-radius:50%;background:var(--charcoal);display:flex;align-items:center;justify-content:center;flex:none}
  .capability__dot svg{width:10px;height:8px}
  .capability--primary .capability__dot{background:var(--plum)}
  .capability--accent .capability__dot{background:var(--orange)}
  .slide--second .capabilities{left:177px;top:309px;width:686px;height:57px;background:none;border-radius:0}
  .capabilities__arrow{position:absolute;inset:0;width:100%;height:100%}

  /* business solutions */
  .solutions{position:absolute;left:188px;top:385px;width:685px;height:85px;border:1px solid var(--line);border-radius:6px;background:var(--white);display:flex;overflow:hidden}
  .solutions__label{width:132px;background:var(--plum);color:var(--white);font-size:21.5px;font-weight:700;line-height:25px;padding:17px 0 0 23px;flex:none}
  .solutions__grid{flex:1;display:grid;grid-template-columns:115px 96px 101px 92px 1fr;grid-template-rows:1fr 1fr}
  .solution{display:flex;align-items:center;gap:6px;padding-left:12px;font-size:8.4px;font-weight:600;color:var(--muted);line-height:10px;border-right:1px solid var(--line);border-bottom:1px solid var(--line);white-space:nowrap}
  .solution b{font-size:14.5px;font-weight:700;color:var(--plum)}
  .solution:nth-child(5n){border-right:0}
  .solution:nth-child(n+6){border-bottom:0}
  .slide--second .solutions{left:177px;top:378px;width:686px;height:96px;border-radius:10px}
  .slide--second .solutions__label{width:136px;font-size:22px;font-weight:500;line-height:27px;padding:23px 0 0 24px}
  .slide--second .solution{border:0}
</style>
</head>
<body>

<svg width="0" height="0" style="position:absolute" aria-hidden="true">
  <defs>
    <symbol id="plane" viewBox="0 0 24 24"><path fill="#fff" d="M21 3.5c-.8-.8-2.2-.7-3 .1l-3.6 3.6L5.6 4.6 3.8 6.4l7.1 4.3-3.6 3.6-2.7-.4-1.4 1.4 3.5 1.9 1.9 3.5 1.4-1.4-.4-2.7 3.6-3.6 4.3 7.1 1.8-1.8-2.6-8.8 3.6-3.6c.8-.8.9-2.2.1-3z"/></symbol>
    <symbol id="bank" viewBox="0 0 24 24"><path fill="#fff" d="M12 3 3 7.5V9h18V7.5zM5 10h2v7H5zm4 0h2v7H9zm4 0h2v7h-2zm4 0h2v7h-2zM3 18h18v2H3z"/></symbol>
    <symbol id="tick-orange" viewBox="0 0 10 8"><polyline points="1,4 4,7 9,1" fill="none" stroke="#F0912C" stroke-width="1.8" stroke-linecap="round" stroke-linejoin="round"/></symbol>
    <symbol id="tick-white" viewBox="0 0 10 8"><polyline points="1,4 4,7 9,1" fill="none" stroke="#fff" stroke-width="1.8" stroke-linecap="round" stroke-linejoin="round"/></symbol>
    <symbol id="ico-card" viewBox="0 0 36 36"><g fill="none" stroke="#fff" stroke-width="1.6" stroke-linejoin="round"><path d="M20 27H3V10h14"/><path d="M3 15h14M6 22h6"/><path d="M26 5l7 3v7c0 5-3 8-7 10-4-2-7-5-7-10V8z"/><polyline points="23,14 25.5,17 29.5,11"/><path d="M33 20v7h-9"/></g></symbol>
    <symbol id="ico-pay" viewBox="0 0 36 36"><g fill="none" stroke="#fff" stroke-width="1.6" stroke-linejoin="round" stroke-linecap="round"><circle cx="18" cy="11" r="8"/><path d="M20.5 8h-3.5a2 2 0 0 0 0 4h2a2 2 0 0 1 0 4h-4M18 6v2M18 16v2"/><path d="M3 27l5-4h7l4 2h-5m0 0h7l7-5c1.5-1 3 1 1.5 2.5L23 30H11l-5 3"/></g></symbol>
    <symbol id="ico-gear" viewBox="0 0 36 36"><g fill="none" stroke="#fff" stroke-width="1.6"><circle cx="18" cy="18" r="5"/><path d="M18 8l2 .3.8 2.3 2 1 2.3-1 2.8 2.8-1 2.3.9 2 2.4.8v4l-2.4.8-.9 2 1 2.3-2.8 2.8-2.3-1-2 .9-.8 2.4h-4l-.8-2.4-2-.9-2.3 1-2.8-2.8 1-2.3-.9-2L8 20v-4l2.4-.8.9-2-1-2.3 2.8-2.8 2.3 1 2-1 .8-2.3z"/><path d="M5 14a14 14 0 0 1 24-7M31 22a14 14 0 0 1-24 7"/></g></symbol>
    <symbol id="ico-cart" viewBox="0 0 36 36"><g fill="none" stroke="#fff" stroke-width="1.6" stroke-linejoin="round" stroke-linecap="round"><path d="M2 6h5l4 18h17l4-13H9"/><path d="M12 18h17"/><circle cx="13" cy="29" r="2.2"/><circle cx="26" cy="29" r="2.2"/></g></symbol>
    <symbol id="ico-globe" viewBox="0 0 36 36"><g fill="none" stroke="#fff" stroke-width="1.6"><circle cx="18" cy="18" r="15"/><ellipse cx="18" cy="18" rx="6.5" ry="15"/><path d="M3 18h30M5.5 10h25M5.5 26h25M18 3v30"/></g></symbol>
  </defs>
</svg>

<!-- ===== Slide one ===== -->
<section class="slide slide--first">
  <aside class="verticals">
    <div class="verticals__head">TARGET CLIENT<br>VERTICALS</div>
    <div class="verticals__notch"></div>
    <div class="vertical" style="top:107px"><span class="vertical__icon"><svg><use href="#plane"/></svg></span>Financial<br>Institutions</div>
    <div class="vertical" style="top:144px"><span class="vertical__icon"><svg><use href="#plane"/></svg></span>Issuers</div>
    <div class="vertical" style="top:183px"><span class="vertical__icon"><svg><use href="#plane"/></svg></span>Acquirers</div>
    <div class="vertical" style="top:219px"><span class="vertical__icon"><svg><use href="#plane"/></svg></span>Banks</div>
    <div class="vertical" style="top:252px"><span class="vertical__icon"><svg><use href="#plane"/></svg></span>FinTechs</div>
    <div class="vertical vertical--indent" style="top:285px"><span class="vertical__icon"><svg><use href="#bank"/></svg></span><span>Airlines</span></div>
    <div class="vertical vertical--indent" style="top:321px"><span class="vertical__icon"><svg><use href="#plane"/></svg></span><span>Hotels</span></div>
    <div class="vertical vertical--indent" style="top:362px"><span class="vertical__icon"><svg><use href="#plane"/></svg></span><span>Merchant<br>Aggregators</span></div>
    <div class="vertical vertical--indent" style="top:408px"><span class="vertical__icon"><svg><use href="#plane"/></svg></span><span>Large<br>Retailers</span></div>
    <div class="vertical vertical--indent" style="top:450px"><span class="vertical__icon"><svg><use href="#plane"/></svg></span><span style="margin-left:8px">SMEs</span></div>
  </aside>

  <h2 class="headline">Business Solutions &amp; <em>Client Verticals</em></h2>

  <div class="service" style="left:190px;width:125px">
    <div class="service__head"><svg><use href="#ico-card"/></svg><h3>Issuer<br>Services</h3></div>
    <ul class="service__rows">
      <li class="service__row"><svg><use href="#tick-orange"/></svg>Debit Card</li>
      <li class="service__row"><svg><use href="#tick-orange"/></svg>Virtual &amp; Prepaid Card</li>
      <li class="service__row"><svg><use href="#tick-orange"/></svg>Credit card</li>
      <li class="service__row"><svg><use href="#tick-orange"/></svg>Corporate Cards</li>
    </ul>
  </div>
  <div class="service service--accent" style="left:323px;width:125px">
    <div class="service__head"><svg><use href="#ico-pay"/></svg><h3>Contactless<br>Payments</h3></div>
    <ul class="service__rows">
      <li class="service__row"><svg><use href="#tick-orange"/></svg>NFC</li>
      <li class="service__row"><svg><use href="#tick-orange"/></svg>E-Wallets</li>
      <li class="service__row"><svg><use href="#tick-orange"/></svg>QR Code</li>
      <li class="service__row"><svg><use href="#tick-orange"/></svg>Tap to Phone</li>
    </ul>
  </div>
  <div class="service service--acquirer" style="left:454px;width:150px">
    <div class="service__head"><svg><use href="#ico-gear"/></svg><h3>Acquirer<br>Services</h3></div>
    <ul class="service__rows">
      <li class="service__row"><svg><use href="#tick-orange"/></svg><span class="pair"><span>Merchant Managmenet</span><span>ATM/Kiosk Acquiring</span></span></li>
      <li class="service__row"><svg><use href="#tick-orange"/></svg><span class="pair"><span>POS/mPOS Acquiring</span><span>ATM Scenario Builder</span></span></li>
      <li class="service__row"><svg><use href="#tick-orange"/></svg><span class="pair"><span>Merchant Loyalty</span><span>ATM/Kiosk Managment</span></span></li>
      <li class="service__row"><svg><use href="#tick-orange"/></svg><span class="pair"><span>Merchant Portal</span><span>ATM/Kiosk Managment</span></span></li>
    </ul>
  </div>
  <div class="service" style="left:610px;width:125px">
    <div class="service__head"><svg><use href="#ico-cart"/></svg><h3>E-Commerce<br>Services</h3></div>
    <ul class="service__rows">
      <li class="service__row"><svg><use href="#tick-orange"/></svg>E-commerce<br>Acquiring</li>
      <li class="service__row"><svg><use href="#tick-orange"/></svg>3D Secure</li>
      <li class="service__row"><svg><use href="#tick-orange"/></svg>BNPL</li>
      <li class="service__row"><svg><use href="#tick-orange"/></svg>Loyalty</li>
    </ul>
  </div>
  <div class="service service--networks" style="left:741px;width:126px">
    <div class="service__head"><svg><use href="#ico-globe"/></svg><h3>Payment<br>Networks</h3></div>
    <ul class="service__rows">
      <li class="service__row">Korvel</li>
      <li class="service__row">Pennant Pay</li>
      <li class="service__row">Tessara</li>
      <li class="service__row">Holmwick</li>
    </ul>
  </div>

  <div class="capabilities">
    <div class="capability capability--primary" style="left:35px"><span class="capability__dot"><svg><use href="#tick-white"/></svg></span>Deep Analytical<br>Services</div>
    <div class="capability capability--accent" style="left:147px"><span class="capability__dot"><svg><use href="#tick-white"/></svg></span>Real-time Fraud<br>Prevention</div>
    <div class="capability" style="left:263px"><span class="capability__dot"><svg><use href="#tick-white"/></svg></span>API Stack</div>
    <div class="capability" style="left:357px"><span class="capability__dot"><svg><use href="#tick-white"/></svg></span>Project &amp; program<br>managment</div>
    <div class="capability" style="left:481px"><span class="capability__dot"><svg><use href="#tick-white"/></svg></span>Solution<br>Consulting</div>
    <div class="capability" style="left:583px"><span class="capability__dot"><svg><use href="#tick-white"/></svg></span>Discovery<br>Workshops</div>
  </div>

  <div class="solutions">
    <div class="solutions__label">Business<br>Solutions</div>
    <div class="solutions__grid">
      <div class="solution"><b>01</b><span>Digital Payment<br>Processing</span></div>
      <div class="solution"><b>03</b><span>Corporate<br>Cards</span></div>
      <div class="solution"><b>05</b><span>Loyalty<br>Monetization</span></div>
      <div class="solution"><b>07</b><span>Travel Cards</span></div>
      <div class="solution"><b>09</b><span>OTP/2FA<br>Passwordless Login</span></div>
      <div class="solution"><b>02</b><span>Fraud Prevention<br>/detection</span></div>
      <div class="solution"><b>04</b><span>Keyless Entry</span></div>
      <div class="solution"><b>06</b><span>Single ID<br>Management</span></div>
      <div class="solution"><b>08</b><span>Fleet &amp;<br>Fuel Cards</span></div>
      <div class="solution"><b>10</b><span>Enhanced Identity<br>Verification</span></div>
    </div>
  </div>
</section>

<!-- ===== Slide two ===== -->
<section class="slide slide--second">
  <aside class="verticals">
    <div class="verticals__head">TARGET CLIENT<br>VERTICALS</div>
    <div class="verticals__notch"></div>
    <div class="vertical" style="top:107px"><span class="vertical__icon"><svg><use href="#plane"/></svg></span>Financial<br>Institutions</div>
    <div class="vertical" style="top:144px"><span class="vertical__icon"><svg><use href="#plane"/></svg></span>Issuers</div>
    <div class="vertical" style="top:183px"><span class="vertical__icon"><svg><use href="#plane"/></svg></span>Acquirers</div>
    <div class="vertical" style="top:219px"><span class="vertical__icon"><svg><use href="#plane"/></svg></span>Banks</div>
    <div class="vertical" style="top:252px"><span class="vertical__icon"><svg><use href="#plane"/></svg></span>FinTechs</div>
    <div class="vertical vertical--indent" style="top:285px"><span class="vertical__icon"><svg><use href="#bank"/></svg></span><span>Airlines</span></div>
    <div class="vertical vertical--indent" style="top:321px"><span class="vertical__icon"><svg><use href="#plane"/></svg></span><span>Hotels</span></div>
    <div class="vertical vertical--indent" style="top:362px"><span class="vertical__icon"><svg><use href="#plane"/></svg></span><span>Merchant<br>Aggregators</span></div>
    <div class="vertical vertical--indent" style="top:408px"><span class="vertical__icon"><svg><use href="#plane"/></svg></span><span>Large<br>Retailers</span></div>
    <div class="vertical vertical--indent" style="top:450px"><span class="vertical__icon"><svg><use href="#plane"/></svg></span><span style="margin-left:8px">SMEs</span></div>
  </aside>

  <h2 class="headline" style="left:170px">Business Solutions &amp; <em>Client Verticals</em></h2>

  <div class="service" style="left:177px;width:126px">
    <div class="service__head"><svg><use href="#ico-card"/></svg><h3>Issuer<br>Services</h3></div>
    <ul class="service__rows">
      <li class="service__row"><svg><use href="#tick-orange"/></svg>Debit Card</li>
      <li class="service__row"><svg><use href="#tick-orange"/></svg>Virtual &amp; Prepaid Card</li>
      <li class="service__row"><svg><use href="#tick-orange"/></svg>Credit card</li>
      <li class="service__row"><svg><use href="#tick-orange"/></svg>Corporate Cards</li>
    </ul>
  </div>
  <div class="service service--accent" style="left:310px;width:127px">
    <div class="service__head"><svg><use href="#ico-pay"/></svg><h3>Contactless<br>Payments</h3></div>
    <ul class="service__rows">
      <li class="service__row"><svg><use href="#tick-orange"/></svg>NFC</li>
      <li class="service__row"><svg><use href="#tick-orange"/></svg>E-Wallets</li>
      <li class="service__row"><svg><use href="#tick-orange"/></svg>QR Code</li>
      <li class="service__row"><svg><use href="#tick-orange"/></svg>Tap to Phone</li>
    </ul>
  </div>
  <div class="service service--acquirer" style="left:445px;width:150px">
    <div class="service__head"><svg><use href="#ico-gear"/></svg><h3>Acquirer<br>Services</h3></div>
    <ul class="service__rows">
      <li class="service__row"><svg><use href="#tick-orange"/></svg><span class="pair"><span>Merchant Managmenet</span><span>ATM/Kiosk Acquiring</span></span></li>
      <li class="service__row"><svg><use href="#tick-orange"/></svg><span class="pair"><span>POS/mPOS Acquiring</span><span>ATM Scenario Builder</span></span></li>
      <li class="service__row"><svg><use href="#tick-orange"/></svg><span class="pair"><span>Merchant Loyalty</span><span>ATM/Kiosk Managment</span></span></li>
      <li class="service__row"><svg><use href="#tick-orange"/></svg><span class="pair"><span>Merchant Portal</span><span>ATM/Kiosk Managment</span></span></li>
    </ul>
  </div>
  <div class="service" style="left:602px;width:127px">
    <div class="service__head"><svg><use href="#ico-cart"/></svg><h3>E-Commerce<br>Services</h3></div>
    <ul class="service__rows">
      <li class="service__row"><svg><use href="#tick-orange"/></svg>E-commerce<br>Acquiring</li>
      <li class="service__row"><svg><use href="#tick-orange"/></svg>3D Secure</li>
      <li class="service__row"><svg><use href="#tick-orange"/></svg>BNPL</li>
      <li class="service__row"><svg><use href="#tick-orange"/></svg>Loyalty</li>
    </ul>
  </div>
  <div class="service service--networks" style="left:736px;width:127px">
    <div class="service__head"><svg><use href="#ico-globe"/></svg><h3>Payment<br>Networks</h3></div>
    <ul class="service__rows">
      <li class="service__row"></li>
      <li class="service__row"></li>
      <li class="service__row"></li>
      <li class="service__row"></li>
    </ul>
  </div>

  <div class="capabilities">
    <svg class="capabilities__arrow" viewBox="0 0 686 57" preserveAspectRatio="none" aria-hidden="true">
      <polygon points="1,28.5 36,1 36,6 650,6 650,1 685,28.5 650,56 650,51 36,51 36,56" fill="#fff" stroke="#DCDCE4" stroke-width="1"/>
    </svg>
    <div class="capability capability--primary" style="left:20px"><span class="capability__dot"><svg><use href="#tick-white"/></svg></span>Deep Analytical<br>Services</div>
    <div class="capability capability--accent" style="left:134px"><span class="capability__dot"><svg><use href="#tick-white"/></svg></span>Real-time Fraud<br>Prevention</div>
    <div class="capability" style="left:254px"><span class="capability__dot"><svg><use href="#tick-white"/></svg></span>API Stack</div>
    <div class="capability" style="left:350px"><span class="capability__dot"><svg><use href="#tick-white"/></svg></span>Project &amp; program<br>managment</div>
    <div class="capability" style="left:478px"><span class="capability__dot"><svg><use href="#tick-white"/></svg></span>Solution<br>Consulting</div>
    <div class="capability" style="left:583px"><span class="capability__dot"><svg><use href="#tick-white"/></svg></span>Discovery<br>Workshops</div>
  </div>

  <div class="solutions">
    <div class="solutions__label">Business<br>Solutions</div>
    <div class="solutions__grid">
      <div class="solution"><b>01</b><span>Digital Payment<br>Processing</span></div>
      <div class="solution"><b>03</b><span>Corporate<br>Cards</span></div>
      <div class="solution"><b>05</b><span>Loyalty<br>Monetization</span></div>
      <div class="solution"><b>07</b><span>Travel Cards</span></div>
      <div class="solution"><b>09</b><span>OTP/2FA<br>Passwordless Login</span></div>
      <div class="solution"><b>02</b><span>Fraud Prevention<br>/detection</span></div>
      <div class="solution"><b>04</b><span>Keyless Entry</span></div>
      <div class="solution"><b>06</b><span>Single ID<br>Management</span></div>
      <div class="solution"><b>08</b><span>Fleet &amp;<br>Fuel Cards</span></div>
      <div class="solution"><b>10</b><span>Enhanced Identity<br>Verification</span></div>
    </div>
  </div>
</section>

</body>
</html>
```